Craft beer label required for new modern craft brewery

I require a label to be designed for my craft beer, the name of the beer is "Tidewalker Pale Ale".
It has to be a contemporary style label targeting an audience group between the ages of 21-40. It must be unique and appealing.
The label must incorporate the image of a Gladiator which has to originally created (I’m giving you creative freedom), not copied (for copy right reasons). I’m attaching a few examples, please refer to “gladiator1.jpg” and “Gladiator2.jpg”.
It would be nice if the Vandrello could appear in the background, also originally created I’m attaching an example, please refer to “Vandrello1.jpg”
The Label must also incorporate the attached logo “Fennmoor Brewing Co. Craft Beer-01.jpg” .
The label must fit a 440ml bottle
Please use creative freedom with regards to the shape of the label.
The colours do not have to be exactly the same as logo, but obviously they must match.
Updates

Target Market(s)

Modern/contemporary successful 21-40 year olds

Industry/Entity Type

Brewery

Font styles to use
Serif
Script

Colors

Designer to choose colors to be used in the design.

Requirements
Must have
• My logo, the beer name and the image of a gladiator
• The label size should be at least 10cm wide x 9cm wide.
• The label must include the size of the bottle: 440ml
• The label must include 6.5% ALC./VOL.
Nice to have
• Vandrello in the back ground
Should not have
• Copied images or trade marks

```html
<!DOCTYPE html>
<html lang="en">
<head>
<meta charset="utf-8">
<title>Tidewalker Pale Ale — Label</title>
<link href="https://fonts.googleapis.com/css2?family=Alfa+Slab+One&family=Lobster&family=Open+Sans:wght@600;700&display=swap" rel="stylesheet">
<style>
  :root {
    --canvas: #ecebe7;
    --label-black: #0d0c0b;
    --gold: #c9a272;
    --gold-dark: #8a6a45;
    --cream: #f4efe6;
    --art-light: #cfc6b6;
    --art-mid: #a39683;
    --art-dark: #5b4d3e;
  }
  * { margin: 0; padding: 0; box-sizing: border-box; }
  html, body { width: 800px; height: 1200px; overflow: hidden; background: var(--canvas); }
  .canvas { position: relative; width: 800px; height: 1200px; }

  /* Neck label */
  .neck-label {
    position: absolute; left: 275px; top: 40px; width: 250px; height: 330px;
    border-radius: 50%; background: var(--label-black);
    border: 3px solid var(--gold-dark);
    display: flex; flex-direction: column; align-items: center;
  }
  .neck-art {
    margin-top: 20px; width: 150px; height: 170px; border-radius: 50% 50% 40% 40%;
    background: radial-gradient(ellipse at 50% 40%, var(--art-light), var(--art-mid) 55%, var(--art-dark));
  }
  .neck-title {
    margin-top: 10px; font-family: "Alfa Slab One", serif; font-size: 34px;
    color: var(--gold); line-height: 1;
  }
  .neck-subtitle {
    font-family: "Lobster", cursive; font-size: 30px; color: var(--cream); line-height: 1.1;
  }

  /* Body label */
  .body-label {
    position: absolute; left: 150px; top: 500px; width: 500px; height: 660px;
    border-radius: 50%; background: var(--label-black);
    border: 4px solid var(--gold-dark);
    display: flex; flex-direction: column; align-items: center;
  }
  .brand-mark {
    position: absolute; left: 50%; top: -110px; transform: translateX(-50%);
    width: 190px; height: 190px; border-radius: 50%;
    background: var(--label-black); border: 4px solid var(--gold);
    display: flex; align-items: center; justify-content: center; text-align: center;
  }
  .brand-name {
    font-family: "Open Sans", sans-serif; font-weight: 700; font-size: 19px;
    letter-spacing: 2px; color: var(--cream); line-height: 1.3; text-transform: uppercase;
  }
  .hero-art {
    margin-top: 90px; width: 420px; height: 340px;
    border-radius: 50% 50% 12% 12% / 60% 60% 12% 12%;
    background: linear-gradient(180deg, var(--art-light) 0%, var(--art-mid) 55%, var(--art-dark) 100%);
  }
  .beer-title {
    margin-top: -30px; font-family: "Alfa Slab One", serif; font-size: 64px;
    color: var(--gold); line-height: 1;
  }
  .beer-style {
    font-family: "Lobster", cursive; font-size: 56px; color: var(--cream); line-height: 1.05;
  }
  .beer-abv {
    font-family: "Open Sans", sans-serif; font-weight: 600; font-size: 18px;
    color: var(--cream); letter-spacing: 1px;
  }
  .beer-volume {
    margin-top: 14px; font-family: "Open Sans", sans-serif; font-weight: 700;
    font-size: 24px; color: var(--cream);
  }
</style>
</head>
<body>
<main class="canvas">
  <section class="neck-label">
    <div class="neck-art" role="img" aria-label="Illustration of a gladiator's helmeted head"></div>
    <p class="neck-title">Tidewalker</p>
    <p class="neck-subtitle">Pale Ale</p>
  </section>

  <section class="body-label">
    <div class="brand-mark">
      <p class="brand-name">Fennmoor<br>Brewing Co.</p>
    </div>
    <div class="hero-art" role="img" aria-label="Illustration of a gladiator with sword standing in the Vandrello arena"></div>
    <h1 class="beer-title">Tidewalker</h1>
    <p class="beer-style">Pale Ale</p>
    <p class="beer-abv">6.5% ALC/VOL</p>
    <p class="beer-volume">440 ml</p>
  </section>
</main>
</body>
</html>
```